Information flyer for 5 day treatment flyer

I am wanting a double sided flyer for my next 5 day treatment program for addictions. I have included the copy for the flyer as an attachment.
I have also included a drop box link to my brand guidelines and my logos. The logo I prefer is the grey horse with the words Willowmere Collective under.
https://www.filecrate.example/sh/k2jtq7wn3xb5lp1/BBQr9TzLm4Kd7c8NpWvY2hsXe?dl=0

https://www.filecrate.example/s/qm8vz2kt6bw9rc4/WILLOWMERE%20COLLECTIVE%20%7C%20Brand%20Identity%20Guidelines.pdf?dl=0
I have also included a copy of an existing flyer which I like very much and a documant with the copy.
https://www.filecrate.example/sh/t7wbn3kx9zq1mv5/CCRt2pLw8-nZ4Kj7FyTuGHs_b?dl=0

I prefer simple, elegant designs please. The design needs to show my clients that I know what I am doing and I am trust worthy and a skilled professional.

Here is the drop box link to the images I have selected for this program. The tones in the images I have selected are orange/red. Please feel free to pick what you think works well.
https://www.filecrate.example/sh/mrq5jv82lnc0tfw/DDDhW392Bx6Lp88_Q7KcZnRye?dl=0

Many thanks
Marisol

```html
<!DOCTYPE html>
<html lang="en">
<head>
<meta charset="utf-8">
<title>Behind Closed Doors – Program Flyer</title>
<link href="https://fonts.googleapis.com/css2?family=Montserrat:wght@200;400;600;700&family=Open+Sans:wght@300;400;600&display=swap" rel="stylesheet">
<style>
:root{
  --navy:#1b2c45;
  --grey-box:rgba(178,173,166,.92);
  --text:#555a62;
  --bg:#ececec;
  --white:#ffffff;
  --sky-top:#3c3d47;
  --sky-glow:#e99a3c;
}
*{box-sizing:border-box;margin:0;padding:0}
html,body{width:800px;height:1200px;overflow:hidden;background:var(--bg)}
body{font-family:"Open Sans",sans-serif;color:var(--text);position:relative}
.page{position:absolute;left:195px;width:410px;height:580px;background:var(--white);overflow:hidden;box-shadow:0 2px 8px rgba(0,0,0,.18)}
.page--front{top:13px}
.page--back{top:607px}
.abs{position:absolute}
.heading{font-family:"Montserrat",sans-serif;font-weight:700;color:var(--navy);text-transform:uppercase;font-size:7px;line-height:1.2;letter-spacing:.2px}
.body-copy{font-size:5.3px;line-height:1.55;font-weight:300;color:var(--text)}
.brand{display:flex;flex-direction:column;align-items:center;gap:5px}
.brand__dot{width:22px;height:22px;border-radius:50%;background:#9a9590}
.brand__name{font-family:"Montserrat",sans-serif;font-weight:400;font-size:6.5px;letter-spacing:1.6px;color:#5a5650}
/* front */
.hero-photo{left:160px;top:0;width:250px;height:268px;border-left:3px solid var(--navy);border-bottom:3px solid var(--navy);
  background:linear-gradient(180deg,#3a3b44 0%,#7b5d4a 35%,#e9a048 58%,#c9742e 72%,#2a1c12 100%)}
.title-box{left:0;top:92px;width:230px;height:106px;background:var(--grey-box);padding:12px 0 0 24px}
.title-box__behind{font-family:"Montserrat",sans-serif;font-weight:200;font-size:40px;letter-spacing:2px;color:var(--white);line-height:1}
.title-box__closed{font-family:"Montserrat",sans-serif;font-weight:700;font-size:24px;color:var(--navy);line-height:1.2}
.tagline{left:25px;top:216px;width:118px;font-size:7.5px;line-height:1.3;color:#444}
.feelings-photo{left:25px;top:405px;width:105px;height:68px;background:linear-gradient(135deg,#2e2118,#8a5a30 55%,#3a2a1c)}
.front-footer{left:0;bottom:0;width:410px;height:34px;background:var(--navy);color:#c9cfd8;font-size:8px;display:flex;align-items:center;justify-content:center;letter-spacing:.3px}
/* back */
.door-photo{left:0;top:0;width:410px;height:200px;background:radial-gradient(ellipse at 50% 62%,#fff3c8 0%,#f2b250 14%,#8a7560 34%,#7d8590 60%,#4d5560 100%)}
.bullets{list-style:none}
.bullets li{font-size:5.2px;line-height:1.5;font-weight:300;color:var(--text);padding-left:4px;position:relative;margin-bottom:1px}
.bullets li::before{content:"•";position:absolute;left:0}
.schedule{width:180px;border-collapse:collapse}
.schedule td{font-size:5.2px;padding:1.6px 6px;color:var(--text)}
.schedule tr:nth-child(odd) td{background:var(--navy);color:#fff}
.schedule tr:nth-child(odd) td:first-child{border-radius:6px 0 0 6px}
.schedule tr:nth-child(odd) td:last-child{border-radius:0 6px 6px 0}
.terms{font-size:3.8px;line-height:1.4;color:#333;font-weight:600}
.back-footer{left:0;bottom:0;width:410px;height:38px;background:var(--navy);color:#dfe3ea;font-size:5px;line-height:1.45;padding:8px 25px}
.contact{position:absolute;right:25px;top:8px;font-size:5.6px;line-height:1.8}
.contact span{display:flex;align-items:center;gap:4px}
</style>
</head>
<body>

<!-- Front side -->
<section class="page page--front">
  <div class="abs brand" style="left:22px;top:22px;width:110px">
    <span class="brand__dot"></span>
    <span class="brand__name">WILLOWMERE COLLECTIVE</span>
  </div>
  <div class="abs hero-photo" role="img" aria-label="Silhouettes of a couple sitting back to back on grass under a golden sunset sky"></div>
  <div class="abs title-box">
    <div class="title-box__behind">BEHIND</div>
    <div class="title-box__closed">Closed Doors</div>
  </div>
  <p class="abs tagline">Break destructive relationship patterns and learn how to create more love and intimacy</p>

  <div class="abs" style="left:25px;top:290px;width:108px">
    <h3 class="heading">What is intimacy?</h3>
    <p class="body-copy" style="margin-top:7px">Intimacy is our emotional food – it sustains and nourishes us, helping us feel connected, understood and valued. Lack of emotional intimacy in our most important relationships creates problems such as anxiety, jealousy, withdrawal, betrayal, abandonment and even infidelity.</p>
  </div>
  <div class="abs feelings-photo" role="img" aria-label="Close-up of printed letters spelling the word Feelings in warm light"></div>

  <div class="abs" style="left:148px;top:290px;width:112px">
    <h3 class="heading">Hunger versus love.</h3>
    <p class="body-copy" style="margin-top:7px">Emotional hunger is not love. This hunger is a strong need caused by emotional deprivation in childhood. Feelings of emotional hunger are experienced as deep internal sensations that range in intensity from a dull ache to a sharp painful feeling. Because of its intensity, this sensation is often confused with real love. Many people claim to be loving and caring, when in fact they are actually feeling their emotional hunger and neediness. Emotional hunger is what we experience when feeling abandonment pain. This keeps us in unfulfilling, destructive and addictive relationships.</p>
  </div>

  <div class="abs" style="left:272px;top:283px;width:116px">
    <h3 class="heading">This program focuses on abandonment and engulfment issues.</h3>
    <p class="body-copy" style="margin-top:6px">To avoid the pain of abandonment and the overwhelming feelings of engulfment, in childhood we subconsciously learn to create a fantasy bond. Later this bond is transferred to our adult relationships, especially romantic and sexual ones. The fantasy bond is a primary defense against intimacy. According to Dr. Alan Whitcombe, "the fantasy bond is a substitute for love and care that was missing in the child's world. Many parents offer affection and love when they feel the need for it themselves. This type of physical affection drains the emotional resources of children rather than nourishing them. It is a form of taking, not giving."</p>
  </div>

  <div class="abs" style="left:25px;top:478px;width:365px">
    <h3 class="heading">Why is it important to examine our childhood when trying to sort out our issues in adult relationships today?</h3>
    <p class="body-copy" style="margin-top:5px">Children are needy by nature, not by choice. They instinctively adapt their behaviour and personalities in order to get their emotional needs met. As a result of the fantasy bond, created between child and caregiver, we carry with us into adulthood the same survival mechanisms leading to a sacrifice of our freedom and any real intimacy in loving relationships. Instead, we create dependencies with people, substances and behaviour patterns to fill the deep emptiness or loneliness within us.</p>
  </div>
  <div class="abs front-footer">Email: marisol@willowmerecollective.com.au</div>
</section>

<!-- Back side -->
<section class="page page--back">
  <div class="abs door-photo" role="img" aria-label="Open white double doors in a wood-panelled room with bright sunset light streaming through"></div>

  <h3 class="abs heading" style="left:25px;top:212px">During the program you will;</h3>
  <ul class="abs bullets" style="left:25px;top:225px;width:175px">
    <li>Identify what you need to do for yourself to stop destructive relationship patterns.</li>
    <li>Learn how to protect yourself from feeling overwhelmed or drained in close relationships.</li>
    <li>Release emotional baggage from past adult relationships.</li>
    <li>Significantly heal childhood abandonment and engulfment issues.</li>
    <li>Identify the subconscious negative beliefs that are sabotaging you from having the relationship you desire.</li>
    <li>Release childhood trauma out of your body from abuse.</li>
  </ul>
  <ul class="abs bullets" style="left:215px;top:225px;width:172px">
    <li>Learn how to set healthy boundaries – physically, emotionally, spiritually, intellectually and sexually.</li>
    <li>Differentiate between needs and values – the drivers in relationships.</li>
    <li>Identify your needs and values and determine steps to take to meet them.</li>
    <li>Free yourself of shame, guilt and fear from childhood and adult relationships.</li>
    <li>Communicate your needs and ask for what you want without feeling too embarrassed or vulnerable.</li>
    <li>Create healthy self-esteem and love – the foundation for intimacy.</li>
  </ul>

  <h3 class="abs heading" style="left:25px;top:322px">Details and cost</h3>
  <h4 class="abs heading" style="left:25px;top:334px;font-size:5.5px">When</h4>
  <table class="abs schedule" style="left:25px;top:343px">
    <tr><td>Thursday 25th October</td><td>6:00pm – 9:00pm</td></tr>
    <tr><td>Friday, 26th October</td><td>9:00am – 5:00pm</td></tr>
    <tr><td>Saturday, 27th October</td><td>9:00am – 9:00pm</td></tr>
    <tr><td>Sunday, 28th October</td><td>9:00am – 5:00pm</td></tr>
    <tr><td>Sunday, 28th October</td><td>9:00pm – 5:00pm</td></tr>
    <tr><td>Monday, 29th October</td><td>9:00am – 4:00pm</td></tr>
  </table>

  <h4 class="abs heading" style="left:25px;top:413px;font-size:5.5px">Inclusions</h4>
  <div class="abs body-copy" style="left:25px;top:421px;width:175px">
    A pre-assessment phone consult<br>Relevant on online diagnostic surveys<br>Integrated Equine Assisted Psychotherapy<br>Roots course<br>All course materials (notebook, writing materials)<br>Morning and afternoon tea daily.
  </div>

  <h4 class="abs heading" style="left:215px;top:334px;font-size:5.5px">Enrolment process</h4>
  <p class="abs body-copy" style="left:215px;top:342px;width:172px">This 5 day program is limited in numbers and offers individual and group time. Enrolments close Friday, 19th October 2018. To book your place, register your interest or find out more about this program please call Marisol 0400 318 274<br>Out of town participants please contact our office for accommodation.</p>

  <p class="abs heading" style="left:215px;top:413px;font-size:5.5px">Investments :<span style="font-weight:400;text-transform:none"> $2250 including GST</span></p>

  <div class="abs brand" style="left:290px;top:430px;width:100px">
    <span class="brand__dot" style="width:18px;height:18px"></span>
    <span class="brand__name" style="font-size:5px">WILLOWMERE COLLECTIVE</span>
  </div>

  <p class="abs terms" style="left:25px;top:520px;width:360px">TERMS &amp; CONDITIONS : A non-refundable deposit of $500 is required to hold your place. Enrolments with full payment is required by Tuesday, 25th October 2018. Card transactions incur a small surcharge. EFTPOS facility available.</p>

  <div class="abs back-footer">
    Willowmere Collective Pty Ltd<br>ABN 12 345 678 901<br>42 Fernbrook Lane, Kurrajong NSW 2758
    <div class="contact">
      <span><svg width="6" height="6" viewBox="0 0 10 10"><path d="M2 0h2l1 3-1.5 1a6 6 0 0 0 2.5 2.5L7 5l3 1v2c0 1-1 2-2 2A8 8 0 0 1 0 2c0-1 1-2 2-2z" fill="#dfe3ea"/></svg>0400 318 274</span>
      <span><svg width="6" height="6" viewBox="0 0 10 10"><rect x="0" y="2" width="10" height="6" fill="none" stroke="#dfe3ea"/><path d="M0 2l5 3 5-3" fill="none" stroke="#dfe3ea"/></svg>marisol@willowmerecollective.com.au</span>
    </div>
  </div>
</section>

</body>
</html>
```